Construction Company Business Card

Business Card Design using new Logo

Contact Information for Business Card

include all company info and website

Requirements
Must have
• Marlon Ridgeway - President
ph. 254-716-5093
Cedar Bend, TX
marlon@stonefieldworks.com
www.stonefieldworks.com

```html
<!DOCTYPE html>
<html lang="en">
<head>
<meta charset="UTF-8">
<title>Stonefield Works – Business Card</title>
<link href="https://fonts.googleapis.com/css2?family=Montserrat:wght@400;500;700&display=swap" rel="stylesheet">
<style>
  :root {
    --page-bg: #efefef;
    --card-dark: #2a2929;
    --card-light: #f7f7f5;
    --brand-red: #c8262b;
    --logo-grey: #c9c9c9;
    --logo-grey-dark: #a9a9a9;
    --ink: #1e1e1e;
    --ink-soft: #333333;
  }
  * { margin: 0; padding: 0; box-sizing: border-box; }
  html, body {
    width: 1200px; height: 900px; overflow: hidden;
    background: var(--page-bg);
    font-family: "Montserrat", sans-serif;
  }
  .stage { position: relative; width: 1200px; height: 900px; }
  .card {
    position: absolute;
    width: 520px; height: 297px;
    top: 302px;
    box-shadow: 0 6px 18px rgba(0,0,0,0.18);
  }
  .card--front { left: 60px; background: var(--card-dark); }
  .card--back { left: 620px; background: var(--card-light); }

  .wordmark {
    position: absolute;
    display: flex; align-items: center; gap: 12px;
    font-weight: 500;
    letter-spacing: 0.12em;
    text-transform: uppercase;
    white-space: nowrap;
  }
  .wordmark__square { width: 12px; height: 12px; background: var(--brand-red); flex: none; }
  .card--front .wordmark {
    left: 50%; top: 50%; transform: translate(-50%, -50%);
    font-size: 30px; color: var(--logo-grey);
  }
  .card--back .wordmark {
    left: 50%; top: 78px; transform: translateX(-50%);
    font-size: 20px; color: var(--logo-grey-dark);
  }

  .person { position: absolute; left: 34px; top: 160px; }
  .person__name {
    font-weight: 700; font-size: 17px; color: var(--ink);
    letter-spacing: 0.01em; text-transform: uppercase;
  }
  .person__title {
    display: inline-block; margin-top: 3px;
    background: var(--brand-red); color: #fff;
    font-size: 12px; font-weight: 400; letter-spacing: 0.04em;
    padding: 2px 8px 2px 6px; text-transform: uppercase;
  }

  .contact {
    position: absolute; right: 30px; bottom: 26px;
    text-align: right; color: var(--ink-soft);
    font-size: 12px; line-height: 1.45;
  }
  .contact__phone { font-size: 13px; margin-bottom: 2px; }
  .contact__place {
    margin-top: 10px; font-weight: 700; color: var(--ink);
    display: inline-flex; align-items: center; gap: 7px;
  }
  .contact__bar { width: 3px; height: 12px; background: var(--brand-red); }
</style>
</head>
<body>
<main class="stage">
  <section class="card card--front" aria-label="Business card front">
    <div class="wordmark"><span class="wordmark__square"></span>Stonefield Works</div>
  </section>

  <section class="card card--back" aria-label="Business card back">
    <div class="wordmark"><span class="wordmark__square"></span>Stonefield Works</div>
    <div class="person">
      <p class="person__name">Marlon Ridgeway</p>
      <span class="person__title">President</span>
    </div>
    <div class="contact">
      <p class="contact__phone">254-716-5093</p>
      <p>marlon@stonefieldworks.com</p>
      <p>www.stonefieldworks.com</p>
      <p class="contact__place">Cedar Bend, TX <span class="contact__bar"></span></p>
    </div>
  </section>
</main>
</body>
</html>
```